Business Card Design Project

Hi,
I am after a business card design for a new business. The business is called Hollow Crest and is a stockist of building supplies used for modern cosmetic renovations for houses. (e.g Floorboards, timber decking, modern fittings and fixtures.)
The logo and font faces have been attached.
The logo comes in 2 different color scheme's - 1. Orange on White & 2. Orange on Black. I would like 2 versions of the business card design to reflect these color scheme's.
The designs need to be double sided. The front should contain all the contact information, whilst the back of the card should display the logo and the URL of the webpage - www.hollowcrest-example.com.au . The logo needs to be displayed creatively on the back of the card.
The business card design needs to reflect the image of modern living, but should also have the wow factor.

```html
<!DOCTYPE html>
<html lang="en">
<head>
<meta charset="utf-8">
<title>Hollow Crest – Business Card Options</title>
<link href="https://fonts.googleapis.com/css2?family=Arimo:wght@400&family=Tinos&display=swap" rel="stylesheet">
<style>
  :root {
    --orange: #e8791d;
    --rust: #a4522a;
    --ink: #222222;
    --grey: #666666;
    --edge: #d4d4d4;
    --paper: #ffffff;
  }
  * { margin: 0; padding: 0; box-sizing: border-box; }
  html, body { width: 1200px; height: 900px; overflow: hidden; background: var(--paper); }
  body { position: relative; font-family: "Arimo", Arial, sans-serif; color: var(--ink); }
  .abs { position: absolute; }
  .option-label { font-size: 20px; color: #000; }
  .side-label { font-size: 15px; color: var(--grey); width: 347px; text-align: center; }
  .card { position: absolute; background: var(--paper); border: 1px solid var(--edge); overflow: hidden; }
  .card svg.shape { position: absolute; left: 0; top: 0; }
  .card .t { position: absolute; font-size: 12px; line-height: 14px; white-space: nowrap; }
  .right { text-align: right; }
  .url { font-family: "Tinos", "Times New Roman", serif; font-size: 11px; color: var(--grey); }
  .t.white, .url.white { color: #fff; }
  .brand { position: absolute; font-size: 27px; line-height: 29px; color: var(--ink); white-space: nowrap; }
  .brand-mark { position: absolute; background: var(--orange); }
</style>
</head>
<body>

  <div class="abs option-label" style="left:97px;top:7px;">Option1</div>

  <!-- Option 1 front -->
  <div class="card" style="left:44px;top:44px;width:348px;height:210px;">
    <svg class="shape" width="348" height="210" viewBox="0 0 348 210" aria-hidden="true">
      <path d="M0,0 H192 C120,22 30,90 0,210 Z" fill="var(--rust)"/>
      <path d="M0,0 H182 C105,18 20,80 0,185 Z" fill="var(--orange)"/>
    </svg>
    <div class="t right" style="right:7px;top:10px;">Your Name</div>
    <div class="brand" style="left:134px;top:74px;">Hollow<br>Crest</div>
    <div class="t right" style="right:7px;top:154px;">Phone: (+61)999-9999<br>Fax: (+61)999-9999<br>your email</div>
    <div class="t" style="left:31px;top:171px;">Your Address<br>City, State and Zip</div>
  </div>
  <div class="abs side-label" style="left:27px;top:255px;">Front</div>

  <!-- Option 1 back -->
  <div class="card" style="left:659px;top:45px;width:345px;height:209px;">
    <div class="brand-mark" style="left:84px;top:68px;width:52px;height:58px;"></div>
    <div class="brand" style="left:148px;top:68px;color:var(--orange);">Hollow<br>Crest</div>
    <div class="t url" style="left:0;width:100%;text-align:center;top:136px;">www.hollowcrest-example.com.au</div>
  </div>
  <div class="abs side-label" style="left:667px;top:256px;">Back</div>

  <div class="abs option-label" style="left:97px;top:283px;">Option2</div>

  <!-- Option 2 front -->
  <div class="card" style="left:44px;top:310px;width:348px;height:199px;">
    <svg class="shape" width="348" height="199" viewBox="0 0 348 199" aria-hidden="true">
      <rect width="348" height="199" fill="var(--orange)"/>
      <path d="M184,0 C150,30 150,80 190,110 C232,140 222,180 250,199 H348 V0 Z" fill="var(--paper)"/>
    </svg>
    <div class="t white" style="left:12px;top:18px;">Your name</div>
    <div class="t white" style="left:13px;top:98px;">Phone:(+61)99-9999999<br>Fax:(+61)99-9999999</div>
    <div class="t white" style="left:13px;top:137px;line-height:13px;">Your Address<br>City, State and Zip<br>Your Email</div>
    <div class="t url white" style="left:13px;top:176px;">www.hollowcrest-example.com.au</div>
    <div class="brand-mark" style="left:229px;top:18px;width:52px;height:58px;"></div>
    <div class="brand" style="left:212px;top:86px;color:var(--ink);">Hollow</div>
    <div class="brand" style="left:234px;top:118px;color:var(--orange);">Crest</div>
  </div>
  <div class="abs side-label" style="left:27px;top:516px;">Front</div>

  <!-- Option 2 back -->
  <div class="card" style="left:659px;top:309px;width:345px;height:208px;">
    <svg class="shape" width="345" height="208" viewBox="0 0 345 208" aria-hidden="true">
      <path d="M0,0 H172 C148,30 148,72 170,102 C196,138 190,176 178,208 H0 Z" fill="var(--orange)"/>
    </svg>
    <div class="brand-mark" style="left:43px;top:55px;width:83px;height:100px;background:var(--paper);"></div>
    <div class="brand" style="left:207px;top:68px;font-size:22px;line-height:29px;color:var(--orange);">Hollow<br>Crest</div>
    <div class="t url" style="right:6px;top:184px;font-size:9.5px;">www.hollowcrest-example.com.au</div>
  </div>
  <div class="abs side-label" style="left:667px;top:517px;">Back</div>

</body>
</html>
```